Ferncrest Dental, LLC business card project

Business card to be designed with current logo.
Dental office- please keep design of card that looks clean and professional.
Please include the following info:
Ferncrest Dental, LLC
Dr. Lorna Pettigrew
2871 Marlowe Street
Bethlehem, PA 18093
610-555-0193
ferncrestdental.office@examplemail.test
Hello everyone-
Reason: Just got back from overseas- will look at all designs and provide feedback. Thank you!
Reason: Polling my friends for the final selection-
thank you to all those that participated- so many talented designers!

```html
<!DOCTYPE html>
<html lang="en">
<head>
<meta charset="utf-8">
<title>Ferncrest Dental, LLC — Business Card</title>
<link rel="stylesheet" href="https://fonts.googleapis.com/css2?family=Source+Sans+3:wght@300;400&display=swap">
<style>
  :root {
    --backdrop: #58585a;
    --card-white: #f7f7f7;
    --card-grey: #e4e4e4;
    --brand-green: #8aae1c;
    --text-green: #74a012;
    --text-grey: #9a9a9a;
    --hill-light: #c9dc00;
    --hill-dark: #8fb51a;
    --panel-light: #c2d800;
    --panel-dark: #659a1f;
    --white: #ffffff;
  }
  * { margin: 0; padding: 0; box-sizing: border-box; }
  html, body {
    width: 1200px; height: 402px; overflow: hidden;
    background: var(--backdrop);
    font-family: "Source Sans 3", "Myriad Pro", sans-serif;
  }
  .canvas { position: relative; width: 1200px; height: 402px; }
  .card {
    position: absolute; top: 30px; width: 524px; height: 302px; overflow: hidden;
    background: radial-gradient(ellipse at 50% 40%, var(--card-white) 40%, var(--card-grey) 100%);
  }
  .card--front { left: 76px; }
  .card--back { left: 632px; }

  .brand {
    display: flex; align-items: center; gap: 10px;
    color: var(--brand-green); font-weight: 300; white-space: nowrap;
  }
  .brand__dot { border-radius: 50%; background: var(--brand-green); flex: none; }

  .card--front .brand {
    position: absolute; left: 0; right: 0; top: 122px; justify-content: center;
    font-size: 38px;
  }
  .card--front .brand__dot { width: 22px; height: 22px; }
  .hill { position: absolute; left: 0; bottom: 0; width: 524px; height: 110px; }

  .card__info { position: absolute; left: 0; top: 0; width: 316px; height: 302px; }
  .card--back .brand { position: absolute; left: 18px; top: 46px; font-size: 22px; gap: 7px; }
  .card--back .brand__dot { width: 12px; height: 12px; }
  .address {
    position: absolute; left: 18px; top: 116px;
    font-style: normal; font-size: 17px; line-height: 24px; color: var(--text-grey);
  }
  .email {
    position: absolute; left: 18px; top: 252px;
    font-size: 14.5px; color: var(--text-green); white-space: nowrap;
  }
  .card__panel {
    position: absolute; right: 0; top: 0; width: 208px; height: 302px;
    background: radial-gradient(circle at 50% 30%, var(--panel-light) 0%, var(--panel-dark) 80%);
  }
  .doctor {
    margin-top: 48px; text-align: center; color: var(--white);
    font-size: 18px; font-weight: 400; white-space: nowrap;
  }
</style>
</head>
<body>
<main class="canvas">
  <section class="card card--front" aria-label="Card front">
    <div class="brand"><span class="brand__dot"></span><span class="brand__name">Ferncrest Dental, LLC</span></div>
    <svg class="hill" viewBox="0 0 524 110" preserveAspectRatio="none" aria-hidden="true">
      <defs>
        <linearGradient id="hillFill" x1="0" y1="0" x2="0" y2="1">
          <stop offset="0" stop-color="var(--hill-dark)"/>
          <stop offset="0.35" stop-color="var(--hill-light)"/>
          <stop offset="1" stop-color="var(--hill-light)"/>
        </linearGradient>
      </defs>
      <path d="M0 56 Q250 -28 524 38 L524 110 L0 110 Z" fill="url(#hillFill)"/>
    </svg>
  </section>

  <section class="card card--back" aria-label="Card back">
    <div class="card__info">
      <div class="brand"><span class="brand__dot"></span><span class="brand__name">Ferncrest Dental, LLC</span></div>
      <address class="address">
        2871 Marlowe Street<br>
        Bethlehem, PA 18093<br>
        610-555-0193
      </address>
      <p class="email">ferncrestdental.office@examplemail.test</p>
    </div>
    <div class="card__panel">
      <p class="doctor">Dr. Lorna Pettigrew</p>
    </div>
  </section>
</main>
</body>
</html>
```